Business card design needed

Looking for an innovative design that portrays a professional image for our company. We are a structural steel erection, EWP and crane hire company. We are looking at having business and contact details on front of card and perhaps a list of what we hire on the back of the card. Our company machine colours are royal blue and silver at present but would be open to change with our cards...
Updates
We are looking for double sided designs due to the amount of information required on the card
The Logo uploaded if the logo we have been using, however our company name has changed to just "Steady Summit Lifting". I have uploaded the image just for ideas...
Reason: Allowing more time for more design submissions
Reason: Want more dedigns
Target Market(s)
Construction/Industrial
Industry/Entity Type
Structural Steel
Contact Information for Business Card
Business Name: Steady Summit Lifting
Specialising in Structural Steel Erection, Equipment & Crane Hire
Address: 27 Corwin Street, Balmoral Q 4571
Site Contact: Dale Morven - 0431 597 203 - dale@sslifting.example
Office Contact: Lina Fairbrook - 0419 735 214 - lina@sslifting.example
We hire Forklifts, Telehandlers, Scissor-lifts, Boom-lifts, 3T Mini Cranes, 16T/20T Bexlo, Prime mover with extendable trailer (13.5-22m), Qualified Boilermakers,Riggers and Dogman.
Logo Text
Steady Summit Lifting or SSL
Logo styles of interest
Emblem Logo
Look and feel

```html
<!DOCTYPE html>
<html lang="en">
<head>
<meta charset="utf-8">
<title>Steady Summit Lifting – Business Card</title>
<link rel="stylesheet" href="https://fonts.googleapis.com/css2?family=Ubuntu:wght@700&family=Open+Sans:wght@400;600;700&display=swap">
<style>
  :root {
    --page: #e9e9eb;
    --royal: #1c2a8c;
    --royal-deep: #10186a;
    --royal-mid: #2a3a9e;
    --gold: #eea20d;
    --navy-text: #1b2a80;
    --white: #ffffff;
    --card-white: #f7f7f7;
    --band: #6d6d70;
    --band-text: #e6e6e6;
  }
  * { box-sizing: border-box; margin: 0; padding: 0; }
  html, body { width: 1200px; height: 900px; overflow: hidden; }
  body {
    background: var(--page);
    display: flex;
    align-items: center;
    justify-content: center;
    gap: 32px;
    font-family: "Open Sans", Arial, sans-serif;
  }
  .card {
    position: relative;
    width: 560px;
    height: 340px;
    overflow: hidden;
    box-shadow: 0 6px 20px rgba(0,0,0,.18);
  }
  .brand-title {
    font-family: "Ubuntu", Arial, sans-serif;
    font-weight: 700;
    color: var(--gold);
    line-height: .98;
  }

  /* Back: hire list */
  .card-back { color: var(--white); }
  .site-photo {
    position: absolute; inset: 0;
    background:
      linear-gradient(160deg, var(--royal-mid) 0%, var(--royal) 45%, var(--royal-deep) 100%);
  }
  .card-back .brand-title {
    position: absolute;
    left: 30px; bottom: 78px;
    font-size: 50px;
  }
  .hire-list {
    position: absolute;
    right: 26px; top: 44px;
    list-style: none;
    text-align: right;
    font-size: 14px;
    line-height: 1.62;
  }
  .hire-list .hire-heading { font-size: 12px; font-weight: 600; letter-spacing: .3px; }

  /* Front: contacts */
  .card-front { background: var(--card-white); color: var(--navy-text); }
  .card-front .brand-title {
    position: absolute;
    left: 34px; top: 30px;
    font-size: 50px;
  }
  .contact {
    position: absolute;
    font-size: 15.5px;
    line-height: 1.3;
  }
  .contact-onsite { left: 34px; top: 172px; }
  .contact-office { left: 310px; top: 104px; }
  .contact-label { font-size: 14px; }
  .contact-name { font-weight: 700; font-size: 18px; letter-spacing: .3px; text-transform: uppercase; margin-top: 2px; }
  .hire-address {
    position: absolute;
    left: 0; right: 0; bottom: 0;
    height: 44px;
    background: var(--band);
    color: var(--band-text);
    font-size: 15px;
    display: flex;
    align-items: center;
    padding-left: 34px;
  }
</style>
</head>
<body>
  <section class="card card-back">
    <div class="site-photo" role="img" aria-label="Blue-toned photo of a crane lifting structural steel on a construction site"></div>
    <h1 class="brand-title">Steady Summit<br>Lifting</h1>
    <ul class="hire-list">
      <li class="hire-heading">WE HIRE:</li>
      <li>• Forklifts • Telehandlers • Scissor-lifts, Boom-lifts</li>
      <li>• 3T Mini Cranes • 16T/20T Bexlo</li>
      <li>• Prime mover with extendable trailer (13.5-22m)</li>
      <li>• Qualified Boilermakers • Riggers and Dogman</li>
    </ul>
  </section>

  <section class="card card-front">
    <h2 class="brand-title">Steady Summit<br>Lifting</h2>
    <div class="contact contact-onsite">
      <p class="contact-label">Onsite Contact Details</p>
      <p class="contact-name">Dale Morven</p>
      <p>Company Director</p>
      <p>M: 0431 597 203</p>
      <p>E: dale@sslifting.example</p>
    </div>
    <div class="contact contact-office">
      <p class="contact-label">Office Contact Details</p>
      <p class="contact-name">Lina Fairbrook</p>
      <p>Office Manager</p>
      <p>M: 0419 735 214</p>
      <p>E: lina@sslifting.example</p>
    </div>
    <p class="hire-address">Hire Address: 27 Corwin Street, Balmoral Q 4571</p>
  </section>
</body>
</html>
```